Redesign website for small print company

Vindaborgprent is a small printing company in Iceland mainly servicing Students, schools, etc. We are also doing all kind of other jobs, like business cards, book printing, brochure printing etc. We are also selling books online.
Our website is: www.vindaborgprent.is
What we are looking for is:
- Web Design (Uncoded - PSD layout only)
- Mobile friendly design, using our current color scheme: Red, green, yellow and light gray.
- Clean simple design
- Simple, light and easy to use.
- More menu Items/drop down
Industry/Entity Type
Digital Printing
Number of Pages Required
5+ page
Requirements
Must have
- Easy navigation
- Designed for mobile
- Current color scheme (see logo)
Nice to have
- Icon based products

```html
<!DOCTYPE html>
<html lang="en">
<head>
<meta charset="utf-8">
<title>Vindaborgprent – Printing for scholars</title>
<link href="https://fonts.googleapis.com/css2?family=Poppins:wght@400;500;600;700&display=swap" rel="stylesheet">
<style>
:root{
  --red:#e3262b;
  --green:#2f9e45;
  --yellow:#f6c200;
  --gray:#f2f2f3;
  --line:#e4e4e6;
  --ink:#1f1f24;
  --muted:#7a7a82;
  --white:#ffffff;
}
*{box-sizing:border-box;margin:0;padding:0}
html,body{width:837px;height:1200px;overflow:hidden}
body{font-family:"Poppins",sans-serif;color:var(--ink);background:var(--white);position:relative}

.topbar{height:34px;display:flex;align-items:center;justify-content:space-between;padding:0 40px;border-bottom:1px solid var(--line);font-size:8px;color:var(--muted)}
.brand{display:flex;align-items:center;gap:6px;font-size:11px;font-weight:600;color:var(--ink)}
.brand-square{width:12px;height:12px;background:var(--red)}
.topbar-contacts{display:flex;gap:18px;align-items:center}
.topbar-contacts span{display:flex;align-items:center;gap:5px}
.topbar-contacts svg{width:9px;height:9px}

.mainnav{height:36px;display:flex;align-items:center;justify-content:center;gap:28px;font-size:9px;font-weight:500;position:relative}
.mainnav .cart{position:absolute;right:40px;top:12px;width:13px;height:13px}

.hero{position:relative;height:210px;text-align:center}
.hero-plant{position:absolute;left:0;top:60px;width:100px;height:150px;border-radius:0 50px 0 0;background:radial-gradient(circle at 40% 40%,#7fb66a,#3f7b3a 70%,#2b5a2a)}
.hero-notebook{position:absolute;right:0;top:-24px;width:170px;height:190px;border-radius:0 0 0 30px;background:linear-gradient(135deg,#f3e4cf,#e6c9a4 55%,#c89c6b)}
.hero h1{position:relative;padding-top:36px;font-size:28px;font-weight:600;line-height:1.25;letter-spacing:-.3px}
.hero-sub{position:relative;margin-top:10px;font-size:9px;color:var(--muted);line-height:1.5}
.search{margin:14px auto 0;width:300px;height:32px;border:1px solid var(--line);border-radius:16px;background:var(--white);display:flex;align-items:center;justify-content:space-between;padding:0 6px 0 16px;font-size:9px;color:var(--muted);box-shadow:0 4px 14px rgba(0,0,0,.08);position:relative}
.search-btn{width:22px;height:22px;border-radius:50%;background:var(--red);display:flex;align-items:center;justify-content:center}

.products{display:grid;grid-template-columns:repeat(3,1fr);gap:12px 26px;padding:20px 60px 0}
.product{display:flex;gap:12px;padding:12px;height:70px}
.product.is-active{box-shadow:0 6px 20px rgba(0,0,0,.1)}
.product svg{flex:none;width:28px;height:32px}
.product h3{font-size:11px;font-weight:500;margin-bottom:4px}
.product p{font-size:7px;color:var(--muted);line-height:1.45}

.btn{display:inline-block;color:var(--white);font-size:8px;font-weight:500;padding:8px 20px;border-radius:14px}
.btn-red{background:var(--red)}
.btn-green{background:var(--green)}
.center{text-align:center}
.products-cta{margin-top:16px}

.books{position:absolute;left:0;top:520px;width:837px;height:410px;background:var(--gray);text-align:center;padding-top:32px}
.books h2{font-size:22px;font-weight:500}
.books-sub{margin:8px auto 0;width:260px;font-size:8px;color:var(--muted);line-height:1.5}
.book-list{display:flex;justify-content:center;gap:14px;margin-top:26px}
.book{width:162px;height:190px;background:var(--white);text-align:left;display:flex;flex-direction:column}
.book-cover{height:90px}
.book-body{padding:8px 10px;flex:1;display:flex;flex-direction:column}
.book h3{font-size:11px;font-weight:500;line-height:1.25}
.book p{font-size:6.5px;color:var(--muted);line-height:1.45;margin-top:4px}
.book .price{margin-top:auto;font-size:9px;font-weight:500}
.books .btn{margin-top:26px}

.footer{position:absolute;left:0;top:930px;width:837px;height:270px;padding:30px 40px;display:grid;grid-template-columns:130px 1fr 150px;gap:24px}
.footer-brand{display:flex;flex-direction:column;align-items:center;padding-top:20px;gap:8px;font-size:11px;font-weight:600}
.footer-brand .brand-square{width:44px;height:44px}
.footer h4{font-size:13px;font-weight:500;margin-bottom:10px}
.about-cols{display:grid;grid-template-columns:1fr 1fr;gap:18px}
.footer p{font-size:7px;color:var(--muted);line-height:1.55;margin-bottom:6px}
</style>
</head>
<body>

<header class="topbar">
  <div class="brand"><span class="brand-square"></span>Vindaborgprent</div>
  <div class="topbar-contacts">
    <span><svg viewBox="0 0 10 10"><path d="M2 1l2 2-1 1.5c.6 1.2 1.3 1.9 2.5 2.5L7 6l2 2-1.2 1.3C4.5 9 1 5.5.7 2.2z" fill="var(--red)"/></svg>555 0142</span>
    <span><svg viewBox="0 0 10 10"><rect x="1" y="2" width="8" height="6" fill="none" stroke="var(--red)"/><path d="M1 2l4 3 4-3" fill="none" stroke="var(--red)"/></svg>info@vindaborgprent.is</span>
    <span><svg viewBox="0 0 10 10"><circle cx="5" cy="5" r="4" fill="none" stroke="var(--red)"/></svg>English</span>
  </div>
</header>

<nav class="mainnav">
  <span>Products</span><span>Books &amp; Resources</span><span>Job opportunities</span><span>Contact</span>
  <svg class="cart" viewBox="0 0 14 14"><path d="M1 2h2l2 7h6l2-5H4" fill="none" stroke="var(--ink)" stroke-width="1.2"/><circle cx="6" cy="12" r="1" fill="var(--ink)"/><circle cx="10" cy="12" r="1" fill="var(--ink)"/></svg>
</nav>

<section class="hero">
  <div class="hero-plant" role="img" aria-label="Green potted plant"></div>
  <div class="hero-notebook" role="img" aria-label="Spiral notebook and pencil on a desk"></div>
  <h1>First-class &amp; Budget-friendly<br>printing for scholars</h1>
  <p class="hero-sub">Budget-friendly prices to ensure your scholar printing needs<br>and to help you bring your documents to life</p>
  <div class="search">What product are you looking for?
    <span class="search-btn"><svg width="10" height="10" viewBox="0 0 10 10"><circle cx="4" cy="4" r="3" fill="none" stroke="#fff" stroke-width="1.3"/><path d="M6.3 6.3L9 9" stroke="#fff" stroke-width="1.3"/></svg></span>
  </div>
</section>

<section class="products">
  <div class="product"><svg viewBox="0 0 28 32"><path d="M2 2h18l6 6v22H2z" fill="var(--red)"/><path d="M20 2v6h6" fill="#f7a3a5"/></svg><div><h3>Essays</h3><p>Clean, affordable printing for essays, reports and course papers of every kind.</p></div></div>
  <div class="product is-active"><svg viewBox="0 0 28 32"><path d="M2 4l8-2v28l-8 2z" fill="var(--red)"/><path d="M10 2l8 2v28l-8-2z" fill="#f07b7e"/><path d="M18 4l8-2v28l-8 2z" fill="var(--red)"/></svg><div><h3>Leaflets</h3><p>Leaflets in all shapes and sizes, from simple handouts to folded promotional prints.</p></div></div>
  <div class="product"><svg viewBox="0 0 28 32"><rect x="1" y="8" width="24" height="15" fill="#f07b7e"/><rect x="3" y="11" width="24" height="15" fill="var(--red)"/></svg><div><h3>Business Cards</h3><p>Sharp, durable business cards with a wide choice of paper and finish.</p></div></div>
  <div class="product"><svg viewBox="0 0 28 32"><path d="M4 3h20v26H4z" fill="var(--red)"/><path d="M4 3h4v26H4z" fill="#b81b20"/></svg><div><h3>Bookprinting</h3><p>Print your theses and books bound to last, in short or long runs.</p></div></div>
  <div class="product"><svg viewBox="0 0 28 32"><rect x="3" y="2" width="22" height="28" fill="var(--red)"/><rect x="7" y="6" width="14" height="10" fill="#f7a3a5"/></svg><div><h3>Posters</h3><p>Posters for presentations, events and exhibitions in vivid colour on quality paper.</p></div></div>
  <div class="product"><svg viewBox="0 0 28 32"><path d="M2 4h11v26H2zM15 4h11v26H15z" fill="var(--red)"/><path d="M13 4h2v26h-2z" fill="#b81b20"/></svg><div><h3>Textbooks</h3><p>Print course textbooks and compendiums quickly, with reliable binding and clear type.</p></div></div>
</section>
<div class="center products-cta"><span class="btn btn-red">All Products</span></div>

<section class="books">
  <h2>Books &amp; Resources</h2>
  <p class="books-sub">A collection of popular books &amp; references for University Students with a wide range of Medical Sciences</p>
  <div class="book-list">
    <article class="book"><div class="book-cover" role="img" aria-label="Book cover for Campus Ventures" style="background:linear-gradient(135deg,#f4efc2,#dfe9a6)"></div><div class="book-body"><h3>Campus Ventures</h3><p>A practical guide to starting and running a student company.</p><span class="price">4.990 kr</span></div></article>
    <article class="book"><div class="book-cover" role="img" aria-label="Book cover for The Craft &amp; Structure of Scholarly Writing" style="background:linear-gradient(135deg,#f8e07a,#e8b93c)"></div><div class="book-body"><h3>The Craft &amp; Structure of Scholarly Writing</h3><p>Clear steps for structuring research papers and building strong arguments.</p><span class="price">5.450 kr</span></div></article>
    <article class="book"><div class="book-cover" role="img" aria-label="Book cover for Numbers: First Steps" style="background:linear-gradient(135deg,#e9e9ec,#c9ccd3)"></div><div class="book-body"><h3>Numbers : First Steps</h3><p>An accessible introduction to core statistical methods for first-year students.</p><span class="price">4.990 kr</span></div></article>
    <article class="book"><div class="book-cover" role="img" aria-label="Book cover for Smarter Budgets" style="background:linear-gradient(135deg,#cfe6c4,#8fc47f)"></div><div class="book-body"><h3>Smarter Budgets</h3><p>Plan a budget, save smarter and understand your money.</p><span class="price">4.990 kr</span></div></article>
  </div>
  <span class="btn btn-green">Book Store</span>
</section>

<footer class="footer">
  <div class="footer-brand"><span class="brand-square"></span>Vindaborgprent</div>
  <div>
    <h4>About the company</h4>
    <div class="about-cols">
      <div><p>Vindaborgprent is a small printing company in Reykjavík that mainly serves students, schools and universities across Iceland. We also handle all kinds of other jobs, from business cards and brochures to book printing.</p><p>Our friendly team offers quick turnaround and fair prices, and we sell books and study resources online.</p></div>
      <div><p>Founded by a group of former students, we know what deadlines feel like. Every order is checked by hand before it leaves the shop, so your work looks its best when it matters most.</p><p>Visit us on campus or order online any time of day.</p></div>
    </div>
  </div>
  <div>
    <h4>Contact info</h4>
    <p>Lindargata 14, 101 Reykjavík<br>Iceland<br>Tel: 555 0142<br>info@vindaborgprent.is<br>www.vindaborgprent.is<br>Mon–Fri 9:00–17:00</p>
  </div>
</footer>

</body>
</html>
```